Help me create an amazing cover for my first ebook!!

I am looking to have a modern and professional looking cover for my first ebook. It will be published through Borvel Lumen Self Press and will need to follow their formatting and guidelines. I want the cover to have a modern and vibrant feel, that appeals to a millennial audience. This is a real estate book that is focused on a niche category catered to young professionals, so the idea would be to appeal to them.

Title:
The Zoomer Primer on Duplex Sharing

The Smartest Property Buying Plan to Start Early, Pay No Rent (or Almost None), and Rocket Boost Your Road to Money Independence.

Dane Wolsky

Target Market(s)

Real Estate investors, investors, millennials, young professionals, college educated, 20-40 years old.Financial freedom, finance.

Industry/Entity Type

Real Estate

Font styles to use
Sans Serif

Colors

Designer to choose colors to be used in the design.

Requirements
Must have
• Must follow the borvel lumen self press format. I attached a screenshot of the details, it can also be found here: https://lsp.borvel.example/en_US/help/topic/Q731920584
• Must include this title:
• The Zoomer Primer on Duplex Sharing
• The Smartest Property Buying Plan to Start Early, Pay No Rent (or Almost None), and Rocket Boost Your Road to Money Independence.
• Dane Wolsky.
• I added examples of book covers I like to use as a guide, I also added some color pallette examples.
Nice to have
• Modern, clean design that's not too busy. Some sort of simple photo or illustration to incorporate in the cover along with the text would be nice.

```html
<!DOCTYPE html>
<html lang="en">
<head>
<meta charset="utf-8">
<title>The Zoomer Primer on Duplex Sharing — Cover</title>
<link rel="stylesheet" href="https://fonts.googleapis.com/css2?family=Fredoka:wght@500;600&display=swap">
<style>
  :root {
    --slate: #3e4254;
    --ink: #454a5c;
    --paper: #f4f4f6;
    --sky-top: #9a99a8;
    --sky-mid: #d6d5de;
    --sky-low: #ecebf0;
    --tower-shade: rgba(70,72,90,0.55);
  }
  * { margin: 0; padding: 0; box-sizing: border-box; }
  html, body { width: 1200px; height: 891px; overflow: hidden; }
  body {
    position: relative;
    background: var(--paper);
    font-family: "Fredoka", sans-serif;
    color: var(--ink);
  }
  .board-left {
    position: absolute; left: 0; top: 0;
    width: 642px; height: 891px;
    background: var(--slate);
  }
  .board-right {
    position: absolute; left: 642px; top: 0;
    width: 558px; height: 891px;
    overflow: hidden;
    background: var(--paper);
  }
  .cover {
    position: absolute; left: 82px; top: 56px;
    width: 471px; height: 751px;
    overflow: hidden;
    background: var(--paper);
    box-shadow: 0 10px 30px rgba(0,0,0,0.45);
  }
  .cover-photo {
    position: absolute; left: 0; top: 0; width: 100%; height: 100%;
    background:
      linear-gradient(180deg, rgba(244,244,246,0) 38%, rgba(244,244,246,0.85) 62%, var(--paper) 80%),
      linear-gradient(90deg, var(--tower-shade) 0%, rgba(0,0,0,0) 24%, rgba(0,0,0,0) 76%, var(--tower-shade) 100%),
      linear-gradient(180deg, var(--sky-top) 0%, var(--sky-mid) 40%, var(--sky-low) 65%, var(--paper) 100%);
  }
  .text-line {
    position: absolute; left: 0; width: 100%;
    text-align: center; line-height: 1;
    transform: translateY(-50%);
    white-space: nowrap;
  }
  .title-main { font-weight: 600; letter-spacing: 0.2px; }
  .title-sub { font-weight: 600; }
  .subtitle {
    position: absolute; left: 50%;
    transform: translateX(-50%);
    text-align: center; font-weight: 600;
  }
  .author { font-weight: 600; }
  .dots { position: absolute; left: 50%; transform: translate(-50%, -50%); }

  .cover .title-main { top: 411px; font-size: 43px; }
  .cover .title-sub { top: 454px; font-size: 27px; }
  .cover .subtitle { top: 488px; width: 400px; font-size: 13.5px; line-height: 20.5px; }
  .cover .dots { top: 566px; }
  .cover .author { top: 654px; font-size: 33px; }

  .board-right .title-main { top: 486px; font-size: 51px; }
  .board-right .title-sub { top: 536px; font-size: 32px; }
  .board-right .subtitle { top: 578px; width: 472px; font-size: 16.5px; line-height: 24.5px; }
  .board-right .dots { top: 671px; }
  .board-right .author { top: 774px; font-size: 39px; }
</style>
</head>
<body>
  <div class="board-left">
    <div class="cover">
      <div class="cover-photo" role="img" aria-label="Upward view of dark glass skyscrapers rising into a pale misty sky"></div>
      <h1 class="text-line title-main">THE ZOOMER PRIMER</h1>
      <h2 class="text-line title-sub">ON DUPLEX SHARING</h2>
      <p class="subtitle">The Smartest Property Buying Plan to Start Early, Pay No Rent (or Almost None), &amp; Rocket Boost Your Road to Money Independence</p>
      <svg class="dots" width="40" height="10" viewBox="0 0 40 10" aria-hidden="true">
        <circle cx="5" cy="5" r="3.6" fill="#454a5c"/>
        <circle cx="20" cy="5" r="3.3" fill="none" stroke="#454a5c" stroke-width="1.2"/>
        <circle cx="35" cy="5" r="3.6" fill="#454a5c"/>
      </svg>
      <p class="text-line author">DANE WOLSKY</p>
    </div>
  </div>

  <div class="board-right">
    <div class="cover-photo" role="img" aria-label="Close view of dark glass skyscrapers rising into a pale misty sky"></div>
    <h1 class="text-line title-main">THE ZOOMER PRIMER</h1>
    <h2 class="text-line title-sub">ON DUPLEX SHARING</h2>
    <p class="subtitle">The Smartest Property Buying Plan to Start Early, Pay No Rent (or Almost None), &amp; Rocket Boost Your Road to Money Independence</p>
    <svg class="dots" width="46" height="12" viewBox="0 0 46 12" aria-hidden="true">
      <circle cx="6" cy="6" r="4.2" fill="#454a5c"/>
      <circle cx="23" cy="6" r="3.9" fill="none" stroke="#454a5c" stroke-width="1.4"/>
      <circle cx="40" cy="6" r="4.2" fill="#454a5c"/>
    </svg>
    <p class="text-line author">DANE WOLSKY</p>
  </div>
</body>
</html>
```